KTR Business Cards

We require business cards for our business. We would like a matte black back to the card, with our logo centred in the middle. The front side of the card is open to design.

Target Market(s)

Clients looking for legal services (professional)

Industry/Entity Type

Legal

Contact Information for Business Card

Dario Velkenor
Partner
Mobile: 0471 386 524
Email: dario@ktrlaw.co
Website: www.ktrlaw.co
Level 3, 118 Pembury Street
Sydney NSW 2000

Font styles to use
Other font styles liked:
• Avenir

Colors
f04a50
ffffff
1b1b1b

Requirements
Must have
• Black back with logo included in the centre of the card.
• Our font is Avenir.

```html
<!DOCTYPE html>
<html lang="en">
<head>
<meta charset="utf-8">
<title>KTR Business Cards</title>
<link href="https://fonts.googleapis.com/css2?family=Nunito+Sans:wght@400;600;800&display=swap" rel="stylesheet">
<style>
  :root {
    --red: #f04a50;
    --white: #ffffff;
    --ink: #1b1b1b;
    --card-black: #141414;
    --backdrop: #242424;
    --muted: #3a3a3a;
  }
  * { box-sizing: border-box; margin: 0; padding: 0; }
  html, body {
    width: 1200px; height: 900px; overflow: hidden;
    background: var(--backdrop);
    font-family: "Nunito Sans", "Avenir", sans-serif;
  }
  .canvas { position: relative; width: 1200px; height: 900px; }
  .card {
    position: absolute; width: 520px; height: 318px;
    border-radius: 3px;
  }
  .card-back {
    left: 60px; top: 150px;
    background: var(--card-black);
    display: flex; align-items: center; justify-content: center;
  }
  .card-front {
    left: 620px; top: 430px;
    background: var(--white);
  }
  .wordmark {
    display: flex; align-items: center; gap: 18px;
  }
  .wordmark-square {
    width: 46px; height: 46px; flex: none;
  }
  .wordmark-name {
    font-weight: 800; text-transform: uppercase;
    line-height: 1.05; letter-spacing: 0.02em;
  }
  .card-back .wordmark-square { background: var(--white); }
  .card-back .wordmark-name { color: var(--white); font-size: 25px; }
  .card-front .wordmark {
    position: absolute; left: 40px; bottom: 46px; gap: 14px;
  }
  .card-front .wordmark-square { width: 34px; height: 34px; background: var(--ink); }
  .card-front .wordmark-name { color: var(--ink); font-size: 18px; }
  .contact {
    position: absolute; left: 262px; top: 44px; color: var(--ink);
  }
  .contact-name {
    font-size: 22px; font-weight: 800; text-transform: uppercase; letter-spacing: 0.01em;
  }
  .contact-name .surname { color: var(--red); }
  .contact-role { font-size: 12px; margin-top: 2px; color: var(--muted); }
  .contact-list { list-style: none; margin-top: 18px; font-size: 12.5px; }
  .contact-list li { display: flex; align-items: center; gap: 9px; line-height: 1.6; }
  .contact-list svg { width: 11px; height: 11px; flex: none; }
  .contact-address { margin-top: 22px; font-size: 12.5px; line-height: 1.55; }
</style>
</head>
<body>
<main class="canvas">
  <section class="card card-back" aria-label="Card back">
    <div class="wordmark">
      <span class="wordmark-square"></span>
      <span class="wordmark-name">Kirwan<br>Tollard<br>Reed</span>
    </div>
  </section>

  <section class="card card-front" aria-label="Card front">
    <div class="contact">
      <h1 class="contact-name">Dario <span class="surname">Velkenor</span></h1>
      <p class="contact-role">Partner</p>
      <ul class="contact-list">
        <li>
          <svg viewBox="0 0 12 12" aria-hidden="true"><path fill="var(--red)" d="M2.5 1l2 2-1 1.3c.6 1.4 1.8 2.6 3.2 3.2l1.3-1 2 2-1.2 1.5C5.4 10 2 6.6 1 2.2z"/></svg>
          0471 386 524
        </li>
        <li>
          <svg viewBox="0 0 12 12" aria-hidden="true"><rect x="1" y="2.5" width="10" height="7" rx="1" fill="var(--red)"/><path d="M1.5 3.2L6 6.5l4.5-3.3" stroke="var(--white)" fill="none" stroke-width="1"/></svg>
          dario@ktrlaw.co
        </li>
        <li>
          <svg viewBox="0 0 12 12" aria-hidden="true"><circle cx="6" cy="6" r="5" fill="var(--red)"/><path d="M1 6h10M6 1c-2 2.5-2 7.5 0 10M6 1c2 2.5 2 7.5 0 10" stroke="var(--white)" fill="none" stroke-width=".8"/></svg>
          www.ktrlaw.co
        </li>
      </ul>
      <p class="contact-address">Level 3, 118 Pembury Street<br>Sydney NSW 2000</p>
    </div>
    <div class="wordmark">
      <span class="wordmark-square"></span>
      <span class="wordmark-name">Kirwan<br>Tollard<br>Reed</span>
    </div>
  </section>
</main>
</body>
</html>
```